New Business Card Design Project

Use the flyer uploaded and website www.brightoakbuilders.com for inspiration.
List Our Services on Backside of business cards
Martin Hollis
Harborline Renovations Inc.
Licensed General Contractors
858-471-9063

Contact Information for Business Card

Use the flyer uploaded and website www.brightoakbuilders.com for inspiration. List Our Services on Backside of business cards Martin Hollis Harborline Renovations Inc. Licensed General Contractors 858-471-9063

```html
<!DOCTYPE html>
<html lang="en">
<head>
<meta charset="utf-8">
<title>Harborline Renovations – Business Cards</title>
<link href="https://fonts.googleapis.com/css2?family=Montserrat:wght@400;500;700&display=swap" rel="stylesheet">
<style>
  :root {
    --bg: #1c1c1e;
    --card: #262628;
    --edge: #3a7fd0;
    --accent: #3b82d4;
    --ink: #f2f2f2;
    --ink-soft: #d9d9d9;
  }
  * { box-sizing: border-box; margin: 0; padding: 0; }
  html, body { width: 1200px; height: 900px; overflow: hidden; }
  body {
    background: var(--bg);
    font-family: "Montserrat", sans-serif;
    color: var(--ink);
    display: flex;
    flex-direction: column;
    align-items: center;
    justify-content: center;
    gap: 36px;
  }
  .card {
    position: relative;
    width: 700px;
    height: 400px;
    background: var(--card);
    border-radius: 26px;
    border-bottom: 5px solid var(--edge);
    box-shadow: 0 12px 30px rgba(0,0,0,.45);
    overflow: hidden;
  }
  .brand-name {
    font-family: "Montserrat", sans-serif;
    font-weight: 400;
    color: var(--ink);
    text-transform: uppercase;
    letter-spacing: 0.14em;
    line-height: 1.35;
  }

  /* Services side */
  .card--services .brand-name {
    position: absolute;
    left: 60px;
    top: 165px;
    width: 300px;
    font-size: 24px;
    text-align: center;
  }
  .card--services .divider {
    position: absolute;
    left: 392px;
    top: 60px;
    width: 1.5px;
    height: 270px;
    background: var(--accent);
  }
  .services {
    position: absolute;
    left: 420px;
    top: 70px;
  }
  .services__title {
    color: var(--accent);
    font-weight: 700;
    font-size: 22px;
    margin-bottom: 10px;
  }
  .services__list { list-style: none; }
  .services__list li {
    font-size: 14.5px;
    line-height: 24px;
    color: var(--ink-soft);
    position: relative;
    padding-left: 16px;
  }
  .services__list li::before {
    content: "";
    position: absolute;
    left: 0;
    top: 10px;
    width: 5px;
    height: 5px;
    border-radius: 50%;
    background: var(--accent);
  }

  /* Contact side */
  .card--contact .brand-name {
    position: absolute;
    right: 60px;
    top: 90px;
    width: 320px;
    font-size: 24px;
    text-align: center;
  }
  .person {
    position: absolute;
    left: 50px;
    top: 218px;
  }
  .person__name {
    color: var(--accent);
    font-weight: 700;
    font-size: 30px;
    line-height: 1.1;
  }
  .person__role {
    font-size: 17px;
    font-weight: 500;
    margin-top: 4px;
  }
  .rule-long {
    position: absolute;
    left: 340px;
    right: 40px;
    top: 262px;
    height: 1.5px;
    background: var(--accent);
  }
  .rule-short {
    position: absolute;
    left: 50px;
    top: 280px;
    width: 150px;
    height: 1.5px;
    background: var(--accent);
  }
  .contacts {
    position: absolute;
    left: 50px;
    top: 292px;
    list-style: none;
  }
  .contacts li {
    display: flex;
    align-items: center;
    gap: 12px;
    font-size: 15px;
    line-height: 27px;
  }
  .contacts svg { width: 14px; height: 14px; fill: var(--accent); }
  .address {
    position: absolute;
    right: 50px;
    top: 282px;
    text-align: right;
    font-size: 15px;
    line-height: 24px;
  }
</style>
</head>
<body>

<section class="card card--services">
  <p class="brand-name">Harborline Renovations</p>
  <div class="divider"></div>
  <div class="services">
    <h2 class="services__title">Our Services</h2>
    <ul class="services__list">
      <li>Remodel: Kitchen &amp; Bath</li>
      <li>Painting: Interior &amp; Exterior</li>
      <li>Flooring: Crapet, Vinyl, Wood</li>
      <li>Window &amp; Door Replacement</li>
      <li>Plumbing: Repair &amp; Upgrades</li>
      <li>Energy Efficienct Upgrades</li>
      <li>Deck &amp; Patio construction</li>
      <li>Water &amp; Mold Damage</li>
      <li>Garage Renovation</li>
    </ul>
  </div>
</section>

<section class="card card--contact">
  <p class="brand-name">Harborline Renovations</p>
  <div class="person">
    <h1 class="person__name">Martin Hollis</h1>
    <p class="person__role">Licensed General Contractors</p>
  </div>
  <div class="rule-long"></div>
  <div class="rule-short"></div>
  <ul class="contacts">
    <li>
      <svg viewBox="0 0 24 24" aria-hidden="true"><path d="M6.6 10.8a15 15 0 0 0 6.6 6.6l2.2-2.2a1 1 0 0 1 1-.25 11.4 11.4 0 0 0 3.6.57 1 1 0 0 1 1 1V20a1 1 0 0 1-1 1A17 17 0 0 1 3 4a1 1 0 0 1 1-1h3.5a1 1 0 0 1 1 1c0 1.25.2 2.45.57 3.6a1 1 0 0 1-.25 1z"/></svg>
      858-471-9063
    </li>
    <li>
      <svg viewBox="0 0 24 24" aria-hidden="true"><path d="M2 5h20v14H2zm2 2v.5l8 5 8-5V7zm0 2.8V17h16V9.8l-8 5z"/></svg>
      info@brightoakbuilders.com
    </li>
    <li>
      <svg viewBox="0 0 24 24" aria-hidden="true"><path d="M12 2a10 10 0 1 0 0 20 10 10 0 0 0 0-20zm6.9 6h-3a15 15 0 0 0-1.3-3.9A8 8 0 0 1 18.9 8zM12 4c.9 1.2 1.6 2.5 2 4h-4c.4-1.5 1.1-2.8 2-4zM4.3 14a8 8 0 0 1 0-4h3.4a16 16 0 0 0 0 4zm.8 2h3a15 15 0 0 0 1.3 3.9A8 8 0 0 1 5.1 16zm3-8h-3a8 8 0 0 1 4.3-3.9A15 15 0 0 0 8.1 8zM12 20c-.9-1.2-1.6-2.5-2-4h4c-.4 1.5-1.1 2.8-2 4zm2.3-6H9.7a14 14 0 0 1 0-4h4.6a14 14 0 0 1 0 4zm.3 5.9a15 15 0 0 0 1.3-3.9h3a8 8 0 0 1-4.3 3.9zm1.7-5.9a16 16 0 0 0 0-4h3.4a8 8 0 0 1 0 4z"/></svg>
      brightoakbuilders.com
    </li>
  </ul>
  <p class="address">84 Meridian Avenue, Suite 210<br>Lakeview, PA 18920</p>
</section>

</body>
</html>
```